Professional and creative business card design for recruiting service providers

Our company supports German medium-sized companies in filling vacancies promptly. For this we use social media marketing and bring our customers into the visibility.

We want a professional but also creative design for our business cards.

Please look at halvenrick-consult.de to get an impression of our CI.

Target Market(s)

Small and medium-sized companies in Germany from the industry

Industry/Entity Type

Industrie, Handwerk

Contact Information for Business Card

Name, Position, Telefonnummer, Email, Website

Colors
EE7325
F08F49
F5BC92
FAE3D3
FDF4ED

Requirements
Must have
• A picture of the employee and in the style of www.halvenrick-consult.de

```html
<!DOCTYPE html>
<html lang="de">
<head>
<meta charset="utf-8">
<title>Halvenrick Consult – Visitenkarte</title>
<link rel="stylesheet" href="https://fonts.googleapis.com/css2?family=Montserrat:wght@400;500;700;800&display=swap">
<style>
  :root {
    --orange: #EE7325;
    --ink: #1e1e1e;
    --panel: #262626;
    --panel-dark: #141414;
    --paper: #ffffff;
    --stage: #c9c9c9;
    --muted: #2b2b2b;
  }
  * { box-sizing: border-box; margin: 0; padding: 0; }
  html, body { width: 1200px; height: 788px; overflow: hidden; }
  body {
    background: var(--stage);
    font-family: "Montserrat", sans-serif;
    display: flex;
    align-items: center;
    justify-content: center;
    gap: 40px;
  }
  .card {
    position: relative;
    width: 540px;
    height: 309px;
    border-radius: 22px;
    overflow: hidden;
    box-shadow: 0 14px 30px rgba(0,0,0,0.25);
  }

  /* Front */
  .card--front { background: var(--paper); }
  .front__band {
    position: absolute; left: 0; right: 0; bottom: 0; height: 112px;
    background: var(--panel);
  }
  .brand {
    position: absolute; left: 34px; top: 44px;
    display: flex; align-items: center; gap: 14px;
  }
  .brand__mark { width: 34px; height: 34px; background: var(--orange); }
  .brand__name {
    font-weight: 800; font-size: 19px; line-height: 1.05;
    letter-spacing: 1.5px; color: var(--ink); text-transform: uppercase;
  }
  .person { position: absolute; left: 34px; top: 128px; }
  .person__name {
    font-weight: 800; font-size: 20px; letter-spacing: 1px;
    color: var(--orange); text-transform: uppercase;
  }
  .person__role { font-weight: 500; font-size: 14px; color: var(--ink); margin-top: 2px; }
  .contact {
    position: absolute; left: 34px; bottom: 18px;
    list-style: none; color: var(--paper); font-size: 13.5px; font-weight: 400;
  }
  .contact li { display: flex; align-items: center; gap: 9px; line-height: 25px; }
  .contact svg { width: 12px; height: 12px; fill: var(--orange); flex: none; }
  .portrait {
    position: absolute; right: 28px; top: 26px; width: 200px; height: 232px;
    background: linear-gradient(180deg, #3a3a3a 0%, #1c1c22 60%, #2a2a30 100%);
    clip-path: polygon(12% 0, 88% 0, 100% 10%, 100% 90%, 88% 100%, 12% 100%, 0 90%, 0 10%);
  }

  /* Back */
  .card--back { background: var(--panel); display: flex; align-items: center; justify-content: center; }
  .back__brand { display: flex; align-items: center; gap: 22px; }
  .back__mark { width: 70px; height: 70px; background: var(--panel-dark); }
  .back__name {
    font-weight: 800; font-size: 34px; line-height: 1.05; letter-spacing: 3px;
    color: var(--panel-dark); text-transform: uppercase;
  }
</style>
</head>
<body>
  <article class="card card--front">
    <div class="front__band"></div>
    <div class="brand">
      <div class="brand__mark"></div>
      <div class="brand__name">Halvenrick<br>Consult</div>
    </div>
    <div class="person">
      <div class="person__name">Lukas Halvenrick</div>
      <div class="person__role">Gründer</div>
    </div>
    <ul class="contact">
      <li><svg viewBox="0 0 24 24"><path d="M6.6 10.8a15.1 15.1 0 0 0 6.6 6.6l2.2-2.2a1 1 0 0 1 1-.25 11.4 11.4 0 0 0 3.6.57 1 1 0 0 1 1 1V20a1 1 0 0 1-1 1A17 17 0 0 1 3 4a1 1 0 0 1 1-1h3.5a1 1 0 0 1 1 1c0 1.25.2 2.45.57 3.57a1 1 0 0 1-.25 1z"/></svg>(123) 456 7890</li>
      <li><svg viewBox="0 0 24 24"><path d="M2 5h20v14H2zm2 2v.5l8 5 8-5V7l-8 5z"/></svg>info@halvenrick-consult.de</li>
      <li><svg viewBox="0 0 24 24"><circle cx="12" cy="12" r="10"/></svg>www.halvenrick-consult.de</li>
    </ul>
    <div class="portrait" role="img" aria-label="Porträtfoto des Gründers im dunklen Sakko am Schreibtisch"></div>
  </article>

  <article class="card card--back">
    <div class="back__brand">
      <div class="back__mark"></div>
      <div class="back__name">Halvenrick<br>Consult</div>
    </div>
  </article>
</body>
</html>
```